Seafood company needs a label design

Our brand name is Coral Pilchards. We need a label design for a new product line of 200g trays of sardine fillets. The label/sleeve is going to wrap around the black tray. We are a family owned and operated business in Esperance, Western Australia. We would like simple appealing designs that catch the eye of the consumer.

Target Market(s)

seafood consumers in supermarkets

Colors

Designer to choose colors to be used in the design.

Requirements
Must have
• The front of the label must include
• •Coral Pilchards
• •since 1997
• •Sustainably wild caught from the pristine southern ocean Esperance Western Australia
Nice to have
• Deep/Rich colours, and black, maybe Drawn picture of sardine/sardines or an anchor fast anchor.
Should not have
• cartoon images, not too cluttered

```html
<!DOCTYPE html>
<html lang="en">
<head>
<meta charset="utf-8">
<title>Coral Pilchards – 200g Tray Label</title>
<link href="https://fonts.googleapis.com/css2?family=Raleway:wght@300;400;800&family=Lora:wght@400&display=swap" rel="stylesheet">
<style>
  :root {
    --canvas-bg: #f1f0ed;
    --label-dark: #2d2c2b;
    --label-dark-deep: #1f1e1d;
    --band-grey: #67635a;
    --band-line: #7d796f;
    --border-line: #5a5753;
    --edge-white: #ffffff;
    --text-light: #f4f2ec;
    --text-soft: #e3e0d8;
    --fish-tone: #4a4844;
    --seal-gold: #c9a13a;
  }
  html, body {
    margin: 0;
    padding: 0;
    width: 1064px;
    height: 1200px;
    overflow: hidden;
    background: var(--canvas-bg);
  }
  .canvas {
    position: relative;
    width: 1064px;
    height: 1200px;
  }
  .tray-label {
    position: absolute;
    left: 152px;
    top: 50px;
    width: 760px;
    height: 1100px;
    display: block;
  }
  .label-edge { fill: none; stroke: var(--edge-white); stroke-width: 6; }
  .label-dark { fill: url(#darkShade); }
  .inner-border { fill: none; stroke: var(--border-line); stroke-width: 2; }
  .fish-art { fill: var(--fish-tone); }
  .name-band { fill: var(--band-grey); }
  .band-rule { stroke: var(--band-line); stroke-width: 2; }
  .wave-edge { fill: none; stroke: var(--edge-white); stroke-width: 6; }
  .brand-light {
    font-family: "Raleway", sans-serif;
    font-weight: 300;
    font-size: 112px;
    fill: var(--text-light);
    letter-spacing: 4px;
  }
  .brand-bold {
    font-family: "Raleway", sans-serif;
    font-weight: 800;
    font-size: 100px;
    fill: var(--text-light);
  }
  .tagline {
    font-family: "Lora", serif;
    font-size: 24px;
    fill: var(--text-soft);
    letter-spacing: 0.5px;
  }
  .since-line {
    font-family: "Raleway", sans-serif;
    font-weight: 400;
    font-size: 17px;
    fill: var(--text-light);
  }
  .quality-seal { fill: var(--seal-gold); }
</style>
</head>
<body>
<main class="canvas">
  <svg class="tray-label" viewBox="0 0 760 1100" xmlns="http://www.w3.org/2000/svg">
    <defs>
      <clipPath id="labelShape">
        <polygon points="100,0 660,0 760,100 760,1070 730,1100 30,1100 0,1070 0,100"/>
      </clipPath>
      <linearGradient id="darkShade" x1="0" y1="0" x2="0" y2="1">
        <stop offset="0" stop-color="#333231"/>
        <stop offset="1" stop-color="#252423"/>
      </linearGradient>
      <linearGradient id="filletTones" x1="0" y1="0" x2="1" y2="0.4">
        <stop offset="0" stop-color="#d9d5c4"/>
        <stop offset="0.45" stop-color="#e6e2d2"/>
        <stop offset="0.7" stop-color="#8a8f90"/>
        <stop offset="0.85" stop-color="#ddd9c8"/>
        <stop offset="1" stop-color="#6d7274"/>
      </linearGradient>
    </defs>

    <g clip-path="url(#labelShape)">
      <g class="fillet-photo" role="img" aria-label="Photograph of pale sardine fillets laid in the tray, silver skin showing">
        <rect x="0" y="700" width="760" height="400" fill="url(#filletTones)"/>
      </g>

      <path class="label-dark" d="M0,100 L100,0 L660,0 L760,100 L760,790 C650,880 520,905 380,865 C240,825 110,765 0,795 Z"/>

      <path class="inner-border" d="M18,760 L18,108 L108,18 L652,18 L742,108 L742,740"/>

      <g class="fish-art" role="img" aria-label="Line drawing of a sardine in side profile">
        <ellipse cx="390" cy="165" rx="270" ry="62" opacity="0.55"/>
      </g>

      <rect class="name-band" x="0" y="330" width="760" height="230"/>
      <line class="band-rule" x1="18" y1="336" x2="742" y2="336"/>
      <line class="band-rule" x1="18" y1="554" x2="742" y2="554"/>

      <text class="brand-light" x="384" y="442" text-anchor="middle">CORAL</text>
      <text class="brand-bold" x="384" y="540" text-anchor="middle" textLength="610" lengthAdjust="spacingAndGlyphs">PILCHARDS</text>

      <text class="tagline" x="380" y="612" text-anchor="middle">Sustainably wild caught from the pristine</text>
      <text class="tagline" x="380" y="644" text-anchor="middle">southern ocean Esperance Western Australia</text>

      <circle class="quality-seal" cx="130" cy="770" r="62"/>

      <path class="wave-edge" d="M0,795 C110,765 240,825 380,865 C520,905 650,880 760,790"/>

      <text class="since-line" x="585" y="828" text-anchor="middle" transform="rotate(-15 585 828)">SINCE 1997  |  NET WT - 200g</text>
    </g>

    <polygon class="label-edge" points="100,3 660,3 757,100 757,1070 730,1097 30,1097 3,1070 3,100"/>
  </svg>
</main>
</body>
</html>
```